Flyer Design Project

We need a flyer and teaser image designed for a March promotional campaign. We have a previous design that just needs a little refresh.
Flyer: the content of the flyer is mostly the same as the pdf you'll see on this link (http://www.morvelbridgemedia.com/Ledger_Pricing.pdf).
Here are the changes: change June to March, change 2011 to 2012, and remove the address of the bottom. I want the color scheme to be consistent with images I attached called "2011 teaser". I need a pdf file.
Teaser Image: the content of the teaser image is the same as "2011 teaser" image I have attached. All that needs to be changed is the month from "June" to "March". I need this to be a .jpg file that's 600x600 pixels.
Please let me know if you have any questions.
Thanks

```html
<!DOCTYPE html>
<html lang="en">
<head>
<meta charset="utf-8">
<title>Digests – March 2012 Pricing</title>
<link href="https://fonts.googleapis.com/css2?family=Chango&family=Lobster&family=Varela+Round&family=Tinos&display=swap" rel="stylesheet">
<style>
  :root {
    --frame-dark: #2b6f82;
    --frame-light: #4b9bb0;
    --panel-top: #e2f6fb;
    --panel-bottom: #b9cfd8;
    --title-fill: #c6dd4a;
    --title-edge: #e2261c;
    --cal-green: #9cc13c;
    --cal-line: #b6b36a;
    --cal-cell: #dcebef;
    --sunday: #c88a24;
    --ink: #111111;
    --orange: #f39a1f;
    --table-green: #c9d95a;
    --table-paper: #f6f6ef;
    --books: #8a6a4a;
  }
  * { box-sizing: border-box; margin: 0; padding: 0; }
  html, body { width: 848px; height: 1200px; overflow: hidden; }
  body {
    background: radial-gradient(ellipse at center, var(--frame-light), var(--frame-dark));
    position: relative;
    font-family: "Tinos", "Times New Roman", serif;
    color: var(--ink);
  }
  .panel {
    position: absolute; left: 21px; top: 19px; width: 804px; height: 1160px;
    background: linear-gradient(180deg, var(--panel-top) 0%, #d3e6ec 45%, var(--panel-bottom) 100%);
  }
  .title {
    position: absolute; top: 18px; left: 0; width: 100%; text-align: center;
    font-family: "Chango", "Cooper Black", serif; font-size: 50px; letter-spacing: 1px;
    color: var(--title-fill); -webkit-text-stroke: 2px var(--title-edge);
  }
  .subtitle {
    position: absolute; top: 92px; left: 0; width: 100%; text-align: center;
    font-family: "Lobster", cursive; font-size: 29px;
    color: var(--title-fill); -webkit-text-stroke: 1.2px var(--title-edge);
  }
  .calendar {
    position: absolute; left: 51px; top: 170px; width: 702px;
    border: 1px solid var(--cal-line);
    font-family: "Varela Round", "Arial Rounded MT Bold", sans-serif;
  }
  .calendar-month {
    height: 31px; background: var(--cal-green); color: #fff;
    text-align: center; font-size: 23px; font-weight: bold; line-height: 31px; letter-spacing: 1px;
  }
  .calendar-grid { display: grid; grid-template-columns: repeat(7, 1fr); }
  .day-name {
    height: 35px; line-height: 35px; text-align: center; font-size: 12px;
    background: #fff; border-right: 1px solid var(--cal-line); border-bottom: 1px solid var(--cal-line);
  }
  .day {
    height: 88px; padding: 10px 0 0; text-align: center;
    font-size: 40px; font-weight: bold; line-height: 1;
    background: var(--cal-cell); border-right: 1px solid var(--cal-line); border-bottom: 1px solid var(--cal-line);
  }
  .day-name:nth-child(7n), .day:nth-child(7n) { border-right: none; }
  .day:nth-last-child(-n+7) { border-bottom: none; }
  .sunday { color: var(--sunday); }
  .details { position: absolute; left: 53px; top: 703px; width: 720px; font-size: 14.6px; line-height: 1.3; }
  .details p { margin-bottom: 17px; }
  .pricing-label { position: absolute; left: 246px; top: 894px; font-size: 33px; }
  .price-box {
    position: absolute; left: 78px; top: 930px; width: 416px; height: 168px;
    background: var(--orange); display: flex; gap: 9px; padding: 0 5px 5px 5px;
  }
  .price-column { flex: 1; display: flex; flex-direction: column; }
  .price-column h3 { height: 47px; line-height: 47px; font-weight: normal; font-size: 23px; padding-left: 40px; }
  .price-column:last-child h3 { padding-left: 55px; }
  .price-head {
    height: 26px; line-height: 26px; background: var(--table-green);
    display: flex; justify-content: space-between; padding: 0 30px 0 8px; font-size: 15px;
  }
  .price-list { flex: 1; background: var(--table-paper); padding: 4px 8px; font-size: 14.2px; line-height: 18.5px; list-style: none; }
  .books {
    position: absolute; left: 562px; top: 930px; width: 180px; height: 164px;
    background: radial-gradient(ellipse at 50% 55%, #b07a4e 0%, #7b6a8f 55%, rgba(185,207,216,0) 75%);
  }
  .contact { position: absolute; left: 0; top: 1112px; width: 100%; text-align: center; font-size: 17.5px; line-height: 23px; }
</style>
</head>
<body>
  <main class="panel">
    <h1 class="title">DIGESTS</h1>
    <p class="subtitle">16 Or 32 pages / 5.5*8.5 Digest</p>

    <section class="calendar">
      <div class="calendar-month">MARCH 2012</div>
      <div class="calendar-grid">
        <div class="day-name">MONDAY</div><div class="day-name">TUESDAY</div><div class="day-name">WEDNESDAY</div><div class="day-name">THURSDAY</div><div class="day-name">FRIDAY</div><div class="day-name">SATURDAY</div><div class="day-name sunday">SUNDAY</div>
        <div class="day"></div><div class="day"></div><div class="day"></div><div class="day">1</div><div class="day">2</div><div class="day">3</div><div class="day sunday">4</div>
        <div class="day">5</div><div class="day">6</div><div class="day">7</div><div class="day">8</div><div class="day">9</div><div class="day">10</div><div class="day sunday">11</div>
        <div class="day">12</div><div class="day">13</div><div class="day">14</div><div class="day">15</div><div class="day">16</div><div class="day">17</div><div class="day sunday">18</div>
        <div class="day">19</div><div class="day">20</div><div class="day">21</div><div class="day">22</div><div class="day">23</div><div class="day">24</div><div class="day sunday">25</div>
        <div class="day">26</div><div class="day">27</div><div class="day">28</div><div class="day">29</div><div class="day">30</div><div class="day">31</div><div class="day"></div>
      </div>
    </section>

    <section class="details">
      <p>Submit your art and order by 3:00 pm EST any business day in March to take advantage of this special pricing.</p>
      <p>Each 16 or 32–page digest includes 70# gloss paper throughout, bleeds and saddle–stitching.</p>
      <p>Your directory will be delivered within 12 business days.</p>
      <p>Note: Although your order may deliver sooner, we cannot accept early delivery requests.</p>
    </section>

    <h2 class="pricing-label" style="font-weight:normal">Pricing</h2>
    <section class="price-box">
      <div class="price-column">
        <h3>16 pages</h3>
        <div class="price-head"><span>Quantity</span><span>Price</span></div>
        <ul class="price-list">
          <li>5,000 ................$1,164.10</li>
          <li>10,000 ..............$1,446.40</li>
          <li>15,000 ..............$1,803.41</li>
          <li>20,000 ..............$2,148.79</li>
        </ul>
      </div>
      <div class="price-column">
        <h3>32 Pages</h3>
        <div class="price-head"><span>Quantity</span><span>Price</span></div>
        <ul class="price-list">
          <li>5,000 ................$1,999.52</li>
          <li>10,000 ..............$2,529.50</li>
          <li>15,000 ..............$3,173.53</li>
          <li>20,000 ..............$3,797.09</li>
        </ul>
      </div>
    </section>
    <div class="books" role="img" aria-label="Illustration of a stack of colourful books with a bookmark"></div>

    <footer class="contact">
      <p>800-555-0142 / 317-555-0186 / f 419-555-0173</p>
      <p>www.morvelbridgemedia.com</p>
    </footer>
  </main>
</body>
</html>
```